SPARK - and the compass of quiet days

I´m writing a book about CHANGE and the skills leaders needs to embody the transformation from being amanager to become leaders.
The title of the book in Icelandic is the same as the name of the project (which I want to be used on the designes is:) HAFALDAN
(with the subtitle:) og listin að hlusta

Change is not controlled or managed – Leading effective change is an art form which is one of the big reasons for why 70% of changes within companies fail. The main reason however, is that managers are tasked with managing and directing them. The art form of change is to put it in the hands of leaders who possess the emotional intelligence that is needed – all their other advantages intact – to lead change all the way.

The big problem when it comes to change is that there are too many managers and too few leaders within companies – leaders who possess emotional intelligence which is the most important skill a leader embodies to empower change. A leader has what it takes to empower followership.

A manager tends to push and control, make decisions that he presupposes others to implement the way he expects. An emotionally competent leader leads by example and enhances followership on that journey because of the trust and respect he has earned.

In few words: SOFT SKILLS ARE THE NEW HARD SKILLS!

```html
<!DOCTYPE html>
<html lang="is">
<head>
<meta charset="utf-8">
<title>Hafaldan – og listin að hlusta</title>
<link rel="stylesheet" href="https://fonts.googleapis.com/css2?family=Bebas+Neue&family=Open+Sans:wght@600;700&display=swap">
<style>
  :root {
    --backdrop: #3b3b3b;
    --paper: #ffffff;
    --paper-shade: #eeeeee;
    --ink: #2b2b38;
    --red-core: #f0301a;
    --red-edge: #c9160c;
    --title-white: #ffffff;
  }
  html, body {
    margin: 0;
    padding: 0;
    width: 1200px;
    height: 1200px;
    overflow: hidden;
    background: var(--backdrop);
  }
  .canvas {
    position: relative;
    width: 1200px;
    height: 1200px;
  }
  .book-cover {
    position: absolute;
    left: 240px;
    top: 50px;
    width: 720px;
    height: 1100px;
    background: linear-gradient(180deg, var(--paper) 0%, var(--paper-shade) 100%);
    overflow: hidden;
  }
  .cover-subtitle {
    position: absolute;
    top: 70px;
    left: 0;
    right: 0;
    margin: 0;
    text-align: center;
    font-family: "Open Sans", sans-serif;
    font-weight: 600;
    font-size: 26px;
    letter-spacing: 4px;
    text-transform: uppercase;
    color: var(--ink);
  }
  .title-stage {
    position: absolute;
    left: 60px;
    top: 240px;
    width: 600px;
    height: 640px;
  }
  .torn-opening {
    position: absolute;
    inset: 0;
    width: 100%;
    height: 100%;
  }
  .cover-title {
    position: absolute;
    inset: 0;
    margin: 0;
    display: flex;
    align-items: center;
    justify-content: center;
    padding-top: 8px;
    font-family: "Bebas Neue", sans-serif;
    font-weight: 400;
    font-size: 150px;
    line-height: 1;
    letter-spacing: 1px;
    color: var(--title-white);
  }
  .cover-author {
    position: absolute;
    left: 0;
    right: 0;
    bottom: 110px;
    margin: 0;
    text-align: center;
    font-family: "Open Sans", sans-serif;
    font-weight: 700;
    font-size: 46px;
    letter-spacing: 3px;
    color: var(--ink);
  }
</style>
</head>
<body>
  <main class="canvas">
    <section class="book-cover">
      <p class="cover-subtitle">og listin að hlusta</p>

      <div class="title-stage">
        <svg class="torn-opening" viewBox="0 0 600 640" role="img" aria-label="Paper torn open revealing a bright red surface behind it">
          <defs>
            <radialGradient id="tear-shadow" cx="50%" cy="50%" r="50%">
              <stop offset="72%" stop-color="#9a9a9a" stop-opacity="0.55"/>
              <stop offset="100%" stop-color="#ffffff" stop-opacity="0"/>
            </radialGradient>
            <radialGradient id="red-surface" cx="50%" cy="45%" r="55%">
              <stop offset="0%" stop-color="var(--red-core)"/>
              <stop offset="100%" stop-color="var(--red-edge)"/>
            </radialGradient>
          </defs>
          <ellipse cx="300" cy="320" rx="300" ry="320" fill="url(#tear-shadow)"/>
          <ellipse cx="300" cy="320" rx="265" ry="280" fill="url(#red-surface)"/>
        </svg>
        <h1 class="cover-title">HAFALDAN</h1>
      </div>

      <p class="cover-author">AUTHOR NAME</p>
    </section>
  </main>
</body>
</html>
```